Bridal Beauty Expert 5 page Website

Modern 5 page website including: home page, Bridal Experts, services, gallery, and book me. Home page to include photo slideshow and contact information for stylist. The Bridal a Experts section will include short biography and photos of each bridal expert 3-4. Services page will include list and description of services and pricing. Gallery will contain work divided in the hair and makeup category. The book me page will contain an active booking tab with drop down service and customer information.

Target Market(s)

Brides, ages 21 to 45

Industry/Entity Type

Hair And Beauty

Coding

Coded - Design and coding required

Number of Pages Required

5+ page

Font styles to use
Serif
Decorative
Script

Colors
faa54b
97b8d9

Requirements
Must have
• Photo slideshow, photo gallery
Nice to have
• Scrolling slide show on home page

```html
<!DOCTYPE html>
<html lang="en">
<head>
<meta charset="utf-8">
<title>Veil &amp; Bloom – About me</title>
<link href="https://fonts.googleapis.com/css2?family=Roboto:wght@300;400;500;700&display=swap" rel="stylesheet">
<style>
:root{
  --orange:#f7a043;
  --orange-soft:#f9c48a;
  --teal:#91ccc6;
  --teal-button:#8ecfca;
  --ink:#3a3a3a;
  --text:#555555;
  --white:#ffffff;
  --blush:#fbeef2;
}
*{box-sizing:border-box;margin:0;padding:0}
html,body{width:840px;height:1200px;overflow:hidden;background:var(--white)}
body{position:relative;font-family:'Roboto',Arial,sans-serif;color:var(--text)}
.abs{position:absolute}

/* navigation */
.nav-button{position:absolute;top:42px;height:26px;border-radius:13px;background:var(--orange);color:var(--white);
  font-size:11.5px;font-weight:500;display:flex;align-items:center;justify-content:center;text-decoration:none}
.nav-button.is-active{background:var(--teal-button)}
.brand{position:absolute;left:353px;top:14px;width:134px;height:82px;border:2px solid var(--teal);border-radius:50%;
  display:flex;align-items:center;justify-content:center;font-size:14px;font-weight:500;color:var(--teal)}

/* hero */
.hero{position:absolute;left:60px;top:109px;width:720px;height:172px;
  background:linear-gradient(90deg,#5a3a22 0%,#8a6a45 25%,#e8c8a6 45%,#c9a276 58%,#6b5a2e 78%,#3d4a22 100%)}
.hero-curve{position:absolute;left:60px;top:230px}

/* intro */
.section-title{position:absolute;left:0;width:840px;top:284px;text-align:center;color:var(--orange);font-size:23px;font-weight:700}
.title-rule{position:absolute;left:395px;top:322px;width:50px;height:2px;background:#8a7a6a}
.intro{position:absolute;left:105px;top:336px;width:630px;text-align:center;font-size:10px;line-height:18px;color:var(--ink)}
.divider{position:absolute;left:300px;top:415px;width:227px;height:1px;background:var(--orange-soft)}
.floral-backdrop{position:absolute;left:0;top:330px;width:840px;height:540px;
  background:radial-gradient(ellipse at 30% 55%,#f8e3ea 0%,rgba(255,255,255,0) 45%),
             radial-gradient(ellipse at 80% 40%,#f6ecef 0%,rgba(255,255,255,0) 40%),
             radial-gradient(ellipse at 55% 75%,#f9e6ec 0%,rgba(255,255,255,0) 45%)}

/* experts */
.expert-photo{position:absolute;width:114px;height:89px;border:1px solid var(--orange)}
.expert-name{position:absolute;font-size:13.5px;color:#222;font-weight:400}
.expert-bio{position:absolute;width:210px;font-size:9.3px;line-height:14px;color:var(--ink)}

/* footer */
.footer{position:absolute;left:60px;top:880px;width:720px;height:300px;background:var(--teal)}
.footer-curve{position:absolute;left:60px;top:879px}
.footer-heading{position:absolute;color:var(--white);font-size:16px;font-weight:400}
.footer-text{position:absolute;color:var(--white);font-size:8.8px;line-height:13.3px}
.social-dot{position:absolute;top:1093px;width:26px;height:26px;border-radius:50%;background:var(--white)}
.post{position:absolute;left:349px;color:var(--white);font-size:8.8px;line-height:14.5px}
.post::before{content:"›";position:absolute;left:0;top:-1px;font-size:12px}
.post span{display:block;padding-left:15px}
.search-box{position:absolute;left:548px;top:992px;width:205px;height:20px;border-bottom:1px solid var(--white);
  color:var(--white);font-size:9px;display:flex;align-items:center}
.contact-line{position:absolute;left:576px;color:var(--white);font-size:11px;line-height:14px}
.contact-icon{position:absolute;left:549px}
</style>
</head>
<body>

<nav>
  <a class="nav-button" style="left:60px;width:60px">Home</a>
  <a class="nav-button is-active" style="left:148px;width:72px">About me</a>
  <a class="nav-button" style="left:249px;width:72px">Services</a>
  <div class="brand">Veil &amp; Bloom</div>
  <a class="nav-button" style="left:521px;width:70px">Gallery</a>
  <a class="nav-button" style="left:623px;width:73px">Book me</a>
  <a class="nav-button" style="left:719px;width:61px">Login</a>
</nav>

<div class="hero" role="img" aria-label="Photo of a bride with an updo in a sunlit garden"></div>
<svg class="hero-curve" width="720" height="52" viewBox="0 0 720 52"><path d="M0 52 Q360 -34 720 52 Z" fill="#fff"/></svg>

<div class="floral-backdrop" role="img" aria-label="Faint pink flower decoration"></div>

<h1 class="section-title">About me</h1>
<div class="title-rule"></div>
<p class="intro">Lorem Ipsum is simply dummy text of the printing and typesetting industry. Lorem Ipsum has been the industry's standard dummy text ever since the 1500s, when an unknown printer took a galley of type and scrambled it to make a type specimen book. It has survived not only five centuries, but also the leap into electronic typesetting, remaining essentially unchanged. It was popularised in the 1960s</p>
<div class="divider"></div>

<section class="experts">
  <div class="expert-photo" style="left:60px;top:459px;background:linear-gradient(135deg,#c79a5a,#e4b990 50%,#5a4030)" role="img" aria-label="Portrait of a blonde bridal expert"></div>
  <h3 class="expert-name" style="left:196px;top:457px">Lorem Ipsum</h3>
  <p class="expert-bio" style="left:196px;top:476px">Lorem Ipsum is simply dummy text of the printing and typesetting industry. Lorem Ipsum has been the industry's standard dummy text ever since the 1500s,Lorem Ipsum Lorem Ipsum is simply dummy .</p>

  <div class="expert-photo" style="left:440px;top:459px;background:linear-gradient(135deg,#2a1c18,#c08a70 50%,#e8e0dc)" role="img" aria-label="Portrait of a dark haired bridal expert"></div>
  <h3 class="expert-name" style="left:576px;top:457px">Lorem Ipsum</h3>
  <p class="expert-bio" style="left:576px;top:476px">Lorem Ipsum is simply dummy text of the printing and typesetting industry. Lorem Ipsum has been the industry's standard dummy text ever since the 1500s,Lorem Ipsum Lorem Ipsum is simply dummy .</p>

  <div class="expert-photo" style="left:60px;top:596px;background:linear-gradient(135deg,#3a2418,#d8a888 55%,#6a4030)" role="img" aria-label="Portrait of a smiling brunette bridal expert"></div>
  <h3 class="expert-name" style="left:196px;top:595px">Lorem Ipsum</h3>
  <p class="expert-bio" style="left:196px;top:614px">Lorem Ipsum is simply dummy text of the printing and typesetting industry. Lorem Ipsum has been the industry's standard dummy text ever since the 1500s,Lorem Ipsum Lorem Ipsum is simply dummy .</p>

  <div class="expert-photo" style="left:440px;top:596px;background:linear-gradient(135deg,#2a2020,#c89078 50%,#3a2a28)" role="img" aria-label="Portrait of a bridal expert with bob haircut"></div>
  <h3 class="expert-name" style="left:576px;top:595px">Lorem Ipsum</h3>
  <p class="expert-bio" style="left:576px;top:614px">Lorem Ipsum is simply dummy text of the printing and typesetting industry. Lorem Ipsum has been the industry's standard dummy text ever since the 1500s,Lorem Ipsum Lorem Ipsum is simply dummy .</p>

  <div class="expert-photo" style="left:60px;top:741px;background:linear-gradient(135deg,#e0e0e0,#b08070 50%,#1e1e1e)" role="img" aria-label="Portrait of a bridal expert in black"></div>
  <h3 class="expert-name" style="left:196px;top:740px">Lorem Ipsum</h3>
  <p class="expert-bio" style="left:196px;top:759px">Lorem Ipsum is simply dummy text of the printing and typesetting industry. Lorem Ipsum has been the industry's standard dummy text ever since the 1500s,Lorem Ipsum Lorem Ipsum is simply dummy .</p>

  <div class="expert-photo" style="left:440px;top:741px;background:linear-gradient(135deg,#f0ece8,#c89478 50%,#4a3028)" role="img" aria-label="Portrait of a bride in a lace veil"></div>
  <h3 class="expert-name" style="left:576px;top:740px">Lorem Ipsum</h3>
  <p class="expert-bio" style="left:576px;top:759px">Lorem Ipsum is simply dummy text of the printing and typesetting industry. Lorem Ipsum has been the industry's standard dummy text ever since the 1500s,Lorem Ipsum Lorem Ipsum is simply dummy .</p>
</section>

<footer>
  <div class="footer"></div>
  <svg class="footer-curve" width="720" height="52" viewBox="0 0 720 52"><path d="M0 0 Q360 100 720 0 Z" fill="#fff"/></svg>

  <h4 class="footer-heading" style="left:91px;top:955px">About us</h4>
  <p class="footer-text" style="left:92px;top:984px;width:212px">We love weddings and all that entails, especially seeing people happily planning the biggest day of their life. We are proud to bring the best people together to make planning that "big day" easier by providing important and reliable resources, answers and solutions.</p>
  <h4 class="footer-heading" style="left:90px;top:1068px">Get Social</h4>
  <div class="social-dot" style="left:91px"></div>
  <div class="social-dot" style="left:120px"></div>
  <div class="social-dot" style="left:147px"></div>
  <div class="social-dot" style="left:175px"></div>
  <div class="social-dot" style="left:204px"></div>
  <div class="social-dot" style="left:233px"></div>
  <div class="social-dot" style="left:262px"></div>
  <p class="footer-text" style="left:90px;top:1145px;font-size:8.5px">Copyright 2015 © Veil &amp; Bloom .All rights reserved.</p>

  <h4 class="footer-heading" style="left:360px;top:955px">Recent Posts</h4>
  <div class="post" style="top:988px"><span>This is a Sticky post</span><span>September 16, 2014</span></div>
  <div class="post" style="top:1024px"><span>This Post Looks Beautiful even<br>Title</span><span>September 12, 2014</span></div>
  <div class="post" style="top:1074px"><span>This is a video Post</span><span>September 11, 2014</span></div>
  <div class="post" style="top:1112px"><span>Satisfaction Lies in the Effort</span><span>August 21, 2014</span></div>

  <h4 class="footer-heading" style="left:548px;top:955px">Search Something</h4>
  <div class="search-box">Search...</div>
  <svg class="abs" style="left:741px;top:995px" width="12" height="12" viewBox="0 0 12 12"><circle cx="5" cy="5" r="3.5" fill="none" stroke="#fff" stroke-width="1.4"/><path d="M7.6 7.6 L11 11" stroke="#fff" stroke-width="1.6"/></svg>

  <svg class="contact-icon" style="top:1030px" width="18" height="17" viewBox="0 0 18 17"><path d="M9 1 L17 8 H15 V16 H11 V11 H7 V16 H3 V8 H1 Z" fill="#fff"/></svg>
  <p class="contact-line" style="top:1032px">2280 Lakeview Drive<br>Suite 118 Maplewood, MN 55109</p>
  <svg class="contact-icon" style="top:1068px" width="17" height="12" viewBox="0 0 17 12"><rect x="0.7" y="0.7" width="15.6" height="10.6" fill="none" stroke="#fff" stroke-width="1.3"/><path d="M1 1 L8.5 7 L16 1" fill="none" stroke="#fff" stroke-width="1.3"/></svg>
  <p class="contact-line" style="top:1067px">hello@veilandbloom.com</p>
  <svg class="contact-icon" style="top:1093px" width="16" height="16" viewBox="0 0 16 16"><path d="M3 1 L6 4 L4.5 6 Q6.5 9.5 10 11.5 L12 10 L15 13 L13 15 Q6 14 1 3 Z" fill="#fff"/></svg>
  <p class="contact-line" style="top:1094px">555.014.2290</p>
  <svg class="contact-icon" style="top:1119px" width="17" height="15" viewBox="0 0 17 15"><path d="M1 5 Q8.5 -1 16 5 L13.5 6.5 L12 4.5 H5 L3.5 6.5 Z" fill="#fff"/><rect x="3.5" y="7" width="10" height="7" rx="1" fill="#fff"/></svg>
  <p class="contact-line" style="top:1121px">555.014.2291</p>
</footer>

</body>
</html>
```